Peter Lanford Studios Business Card

Looking for a clear, modern, elegant, sharp business card that conveys a professional yet edgy image to my business as a wedding, portrait, and travel photographer. Would like something that looks vintage yet modern. Need a new business card to grow my business. We are growing the business for Wedding and Event Photography as well as fine art Photography. (Mostly Landscapes)
Updates

I’m looking through designs now but I have a new logo that i want using please.

New logo uploaded please redesign using that

PLEASE ALL DESIGNERS LOOK IN BRIEF FOR NEW LOGO

Target Market(s)

Brides, Grooms, Families with Kids, People looking for Fine Art Photography Artwork

Industry/Entity Type

Photographer

Contact Information for Business Card

Unsure

Font styles to use
Serif

Colors

Designer to choose colors to be used in the design.

Requirements
Must have
• My Website:
• http://lanfordgallery.snapfolio.example
• Phone:
• 555-418-2061
• Email:
• petelanfordgallery@mailbox.example
Nice to have
• Would like a sort of shine on the printing finish.
• I like black I think it looks good on a business card.
• Can try working with my logo (png that I've attached)

```html
<!DOCTYPE html>
<html lang="en">
<head>
<meta charset="utf-8">
<title>Peter Lanford Studios Business Card</title>
<link href="https://fonts.googleapis.com/css2?family=Hind:wght@400&display=swap" rel="stylesheet">
<style>
  :root {
    --backdrop: #e6e6e6;
    --card-dark: #161619;
    --card-light: #ffffff;
    --logo-grey: #bcbcbe;
    --ink: #1e1e1e;
  }
  * { margin: 0; padding: 0; box-sizing: border-box; }
  html, body {
    width: 1200px;
    height: 896px;
    overflow: hidden;
    background: var(--backdrop);
    font-family: "Hind", Arial, sans-serif;
  }
  .canvas {
    position: relative;
    width: 1200px;
    height: 896px;
  }
  .card {
    position: absolute;
    left: 354px;
    width: 484px;
    height: 277px;
    border-radius: 30px;
    display: flex;
    flex-direction: column;
    align-items: center;
    justify-content: center;
  }
  .card--front {
    top: 162px;
    background: var(--card-dark);
  }
  .card--back {
    top: 470px;
    background: var(--card-light);
  }
  .brand {
    color: var(--logo-grey);
    font-weight: 400;
    text-align: center;
    text-transform: uppercase;
    margin-top: -10px;
  }
  .brand__name {
    display: block;
    font-size: 23px;
    letter-spacing: 0.2em;
    margin-right: -0.2em;
    line-height: 1;
  }
  .brand__tag {
    display: block;
    font-size: 8.5px;
    letter-spacing: 0.38em;
    margin-right: -0.38em;
    margin-top: 8px;
  }
  .contact {
    color: var(--ink);
    font-size: 12.5px;
    letter-spacing: 0.06em;
    line-height: 22px;
    text-align: center;
    margin-top: -4px;
  }
  .contact__line { display: flex; justify-content: center; align-items: center; }
  .contact__sep { margin: 0 10px; }
  .contact__mark {
    display: inline-block;
    width: 9px;
    height: 9px;
    background: var(--ink);
    margin-right: 3px;
    margin-top: -2px;
  }
</style>
</head>
<body>
<main class="canvas">
  <section class="card card--front" aria-label="Card front">
    <h1 class="brand">
      <span class="brand__name">Peter Lanford</span>
      <span class="brand__tag">Studios</span>
    </h1>
  </section>
  <section class="card card--back" aria-label="Card back">
    <address class="contact" style="font-style:normal">
      <div class="contact__line">
        <span class="contact__phone">555-418-2061</span>
        <span class="contact__sep">|</span>
        <span class="contact__email">petelanfordgallery@mailbox.example</span>
      </div>
      <div class="contact__line">
        <span class="contact__web">lanfordgallery.snapfolio.example</span>
        <span class="contact__sep">|</span>
        <span class="contact__mark" aria-hidden="true"></span>
        <span class="contact__handle">@petelanfordgallery</span>
      </div>
    </address>
  </section>
</main>
</body>
</html>
```